■目的・概要 ・QPKへの出稿用バナー作成をしていただける方を募集します。 ■依頼詳細 ・バナー内にテキストを挿入する場合は、テキストレイヤーで挿入してください。 テキストはおよそ1/4サイズで表示される事を考慮して制作して下さい。 ・サイト内の画像を使用し、制作をお願いします。 ・内祝いギフトのページなので 内祝いギフト用のバナーをお願いいたします。 ・サイト内の商品を見ていただき、販促につながるバナー制作をお願いします。 ■参考サイト(配信サイト) http://mova-gift.example/sakura ■サイズと枚数 ・1200 x 628 ・1枚 ■納品ファイル ・フォトショップ形式(.psd) ■注意点・禁止事項 土日・祝日は対応することができません。 平日は9~19時までにご連絡いただければ、当日。 それ以降は翌日にご返信いたします。 ※Zelmo QPKガイドラインに沿った内容である事 QPK掲載ガイドライン関連資料(http://adinfo.zelmo.example/online/doc/pdf_guideline.html) ※他で登録されているデザインや商標の転用など、他社の知的財産権を侵すこと ※他のクライアントへ既に提案した内容の転用など たくさんのウェブデザイナーの方からのご提案をお待ちしております。 |
バナーの落ち着いた雰囲気から選ばせて頂きました。
非常にレベルの高い提案をたくさん頂き本当に感謝しております。どうせであれば全部採用したいのですが、今回は1種類のみ選ばせて頂きました。
これからも募集していきますので、引き続き、よろしくお願いします。

```html
<!DOCTYPE html>
<html lang="ja">
<head>
<meta charset="utf-8">
<title>内祝・寿 ギフトセット バナー</title>
<link href="https://fonts.googleapis.com/css2?family=Noto+Sans+JP:wght@500;700;900&display=swap" rel="stylesheet">
<style>
  :root {
    --bg: #ffffff;
    --ink: #4a3322;
    --ink-dark: #2f2218;
    --accent: #e67e17;
    --accent-red: #c0392b;
    --line: #cfc6bb;
    --photo-a: #f3ece0;
    --photo-b: #d9c39a;
  }
  * { margin: 0; padding: 0; box-sizing: border-box; }
  html, body { width: 1200px; height: 628px; overflow: hidden; background: var(--bg); }
  .banner {
    position: relative; width: 1200px; height: 628px; overflow: hidden;
    font-family: "Noto Sans JP", sans-serif; color: var(--ink);
    background: var(--bg);
  }
  .brand {
    position: absolute; left: 20px; top: 40px; width: 210px;
    display: flex; flex-direction: column; align-items: center; gap: 4px;
  }
  .brand-mark { width: 36px; height: 36px; border-radius: 50%; background: var(--photo-b); }
  .brand-name { font-size: 58px; font-weight: 700; color: var(--ink); letter-spacing: 4px; line-height: 1; }
  .brand-kana { font-size: 22px; font-weight: 700; color: var(--ink); letter-spacing: 6px; }
  .tagline {
    position: absolute; left: 262px; top: 16px; width: 930px;
    font-size: 22px; font-weight: 700; color: var(--accent-red); white-space: nowrap;
    text-align: center; line-height: 1.2;
  }
  .perk {
    position: absolute; top: 62px; height: 126px;
    border: 2px solid var(--line); border-radius: 6px; padding: 8px 12px;
  }
  .perk-label { font-size: 20px; font-weight: 700; color: var(--ink-dark); white-space: nowrap; text-align: center; }
  .perk-body { display: flex; align-items: center; justify-content: center; gap: 18px; margin-top: 8px; height: 66px; }
  .perk-big { font-size: 56px; font-weight: 900; color: var(--accent); line-height: 1; }
  .perk-small { font-size: 28px; font-weight: 900; color: var(--accent); }
  .perk-mid { font-size: 34px; font-weight: 900; color: var(--accent); }
  .perk--free { left: 256px; width: 270px; }
  .perk--sale { left: 538px; width: 324px; }
  .perk--zero { left: 874px; width: 318px; }
  .divider { position: absolute; left: 256px; right: 8px; top: 196px; height: 2px; background: var(--line); }
  .photo {
    position: absolute; border: 2px solid var(--line);
    background: linear-gradient(135deg, var(--photo-a) 0%, var(--photo-b) 100%);
  }
  .photo--main { left: 190px; top: 202px; width: 354px; height: 206px; }
  .photo--left { left: 60px; top: 414px; width: 264px; height: 200px; }
  .photo--right { left: 334px; top: 414px; width: 262px; height: 200px; }
  .title {
    position: absolute; left: 566px; top: 208px; width: 620px;
    font-size: 54px; font-weight: 900; color: var(--ink); white-space: nowrap; letter-spacing: 1px;
  }
  .price { position: absolute; left: 566px; top: 290px; width: 284px; text-align: center; color: var(--accent); }
  .price-main { font-size: 76px; font-weight: 900; line-height: 1.05; white-space: nowrap; }
  .price-main small { font-size: 52px; }
  .price-tax { font-size: 28px; font-weight: 700; white-space: nowrap; }
  .contents {
    position: absolute; left: 852px; top: 300px; width: 330px; height: 178px;
    border: 3px solid var(--ink); padding: 8px 18px;
  }
  .contents li { list-style: none; font-size: 34px; font-weight: 700; color: var(--ink); line-height: 1.22; white-space: nowrap; }
  .contents .note { font-size: 22px; line-height: 1.6; }
  .cta {
    position: absolute; left: 768px; top: 552px; width: 414px;
    display: flex; align-items: center; justify-content: flex-end; gap: 18px;
    font-size: 34px; font-weight: 700; color: var(--ink); white-space: nowrap;
  }
</style>
</head>
<body>
<main class="banner">
  <div class="brand">
    <span class="brand-mark"></span>
    <span class="brand-name">MOVA</span>
    <span class="brand-kana">モーヴァ</span>
  </div>

  <p class="tagline">『宅配無料』のギフトセットが格安！お得なギフトは【モーヴァ】にお任せください！</p>

  <section class="perk perk--free">
    <p class="perk-label">結婚式のギフトセット宅配</p>
    <div class="perk-body">
      <svg width="96" height="56" viewBox="0 0 96 56" aria-hidden="true">
        <rect x="2" y="4" width="58" height="38" fill="#6b4a2e"/>
        <path d="M62 16 H80 L92 30 V42 H62 Z" fill="#6b4a2e"/>
        <rect x="68" y="20" width="12" height="9" fill="#fff"/>
        <circle cx="20" cy="46" r="8" fill="#2f2218"/>
        <circle cx="76" cy="46" r="8" fill="#2f2218"/>
      </svg>
      <span class="perk-big">無料</span>
    </div>
  </section>

  <section class="perk perk--sale">
    <p class="perk-label">人気商品を年中大特価でご奉仕!</p>
    <div class="perk-body">
      <span class="perk-small">最大</span><span class="perk-big" style="margin-left:-14px">50</span><span class="perk-small" style="margin-left:-14px">%OFF</span>
    </div>
  </section>

  <section class="perk perk--zero">
    <p class="perk-label">挨拶状やのしなど印刷代込みで</p>
    <div class="perk-body">
      <svg width="62" height="62" viewBox="0 0 62 62" aria-hidden="true">
        <rect x="6" y="24" width="50" height="34" fill="#e8a24a"/>
        <rect x="2" y="16" width="58" height="12" fill="#e67e17"/>
        <rect x="26" y="16" width="10" height="42" fill="#c0392b"/>
        <path d="M31 16 C20 2 8 8 18 16 Z M31 16 C42 2 54 8 44 16 Z" fill="#c0392b"/>
      </svg>
      <span class="perk-mid">すべて</span><span class="perk-big">0円</span>
    </div>
  </section>

  <div class="divider"></div>

  <div class="photo photo--main" role="img" aria-label="和紙箱に紅白の水引を掛けたギフトセットと、茶器・菓子などの内容品の写真"></div>
  <div class="photo photo--left" role="img" aria-label="水引付きギフト箱と急須・湯呑などのサブギフトの写真"></div>
  <div class="photo photo--right" role="img" aria-label="水引付きギフト箱と漆器の椀・菓子詰め合わせの写真"></div>

  <h1 class="title">内祝・寿 ギフトセット</h1>

  <div class="price">
    <p class="price-main">5,000<small>円</small></p>
    <p class="price-tax">(税込5,400円)</p>
  </div>

  <ul class="contents">
    <li>A メインギフト</li>
    <li>B 引菓子</li>
    <li>C サブギフト</li>
    <li class="note">※お礼状・豪華和紙箱付</li>
  </ul>

  <p class="cta">詳しくはこちらから
    <svg width="30" height="34" viewBox="0 0 30 34" aria-hidden="true"><path d="M2 2 L28 17 L2 32 Z" fill="#4a3322"/></svg>
  </p>
</main>
</body>
</html>
```